Revamp Current Website From 2012 TO 2018

We need a ravamp to our current website. I prefer a professional corporate modern feel to it.

My Current Website is www.brightlanepromoworks.biz. Please redesign the homepage and the /certs page first....see attached document for specific instructions..

There is a lot of content at the bottom but maybe we can shorten that by using titles and a pop up of the details or something so it doesnt take too mcuh space...or maybe a red more hyperlink to see the rest of info in pop up or something or new page...

Target Market(s)

B2B, business owners, website owners, marketing companies.

Industry/Entity Type

Promotional Product

Number of Pages Required

2 page

Colors

Designer to choose colors to be used in the design.

Requirements
Must have
• Please keep in mind logo mock up I am working on that looks beautiful on dark background for header...see attached for logo
• Must use existing content I hope your marketing mind comes in to play when designing the website.
• Must have all my content provided on each page...
Nice to have
• similiar color scheme...
Should not have
• I dont like using templates because usually hard to expand on design in future so Prefer full custom designs
• Please no templates

```html
<!DOCTYPE html>
<html lang="en">
<head>
<meta charset="utf-8">
<title>Brightlane Promo Works – Promotional Incentives</title>
<link href="https://fonts.googleapis.com/css2?family=Raleway:wght@400;500;600&family=Open+Sans:wght@400;600;700&display=swap" rel="stylesheet">
<style>
:root{
  --blue:#0a63d8;
  --blue-deep:#0a3fae;
  --navy:#0a1a3c;
  --ink:#333a44;
  --muted:#6a7380;
  --light:#f3f4f6;
  --white:#ffffff;
  --footer:#0d1626;
  --footer-bottom:#0a111e;
}
*{box-sizing:border-box;margin:0;padding:0}
html,body{width:1200px;height:4539px;overflow:hidden}
body{font-family:"Open Sans",Arial,sans-serif;color:var(--ink);background:var(--white);position:relative}
.section{position:absolute;left:0;width:1200px;overflow:hidden}
h1,h2,h3,.headline{font-family:"Raleway",Arial,sans-serif;font-weight:500}
.btn{display:inline-block;font-size:13px;font-weight:600;padding:11px 0;text-align:center;border-radius:2px;text-decoration:none}
.btn-blue{background:var(--blue);color:var(--white)}
.btn-white{background:var(--white);color:var(--blue-deep)}
.btn-outline{border:1px solid var(--white);color:var(--white);background:var(--white);color:var(--ink)}
.fill{position:absolute;inset:0}

/* hero */
.hero{top:0;height:592px}
.hero .fill{background:linear-gradient(180deg,#1c2a48 0%,#3b4566 30%,#b86a4a 58%,#d98a4c 66%,#3a3e58 80%,#1a1f33 100%)}
.topbar{position:absolute;top:0;left:0;width:1200px;height:70px;background:rgba(8,14,30,.55)}
.brand{position:absolute;left:97px;top:20px;display:flex;align-items:center;gap:10px;color:var(--white);font-family:"Raleway",sans-serif;font-size:20px;font-weight:600;letter-spacing:.5px}
.brand .mark{width:22px;height:22px;background:var(--blue)}
.nav{position:absolute;top:28px;left:437px;display:flex;gap:34px;font-size:13px;color:#dfe4ee}
.nav .active{color:#5aa2ff}
.contact-line{position:absolute;top:96px;left:120px;font-size:12px;color:var(--white);display:flex;gap:24px}
.hero-copy{position:absolute;right:100px;top:212px;width:600px;text-align:right;color:var(--white)}
.hero-copy h1{font-size:27px;line-height:1.3;font-weight:400}
.hero-copy p{font-size:12px;line-height:1.6;margin-top:22px}
.hero-copy .strong{font-weight:700;margin-top:10px}
.hero-actions{position:absolute;top:425px;left:720px;display:flex;gap:33px}

/* stats */
.stats{top:592px;height:250px;background:linear-gradient(90deg,#0a56d0,#0f6ee6)}
.stat{position:absolute;top:60px;width:220px;text-align:center;color:var(--white)}
.stat .num{font-family:"Raleway",sans-serif;font-size:38px;margin-top:6px}
.stat .label{font-size:13px;margin-top:4px}

/* incentives */
.incentives{top:842px;height:540px;background:var(--light)}
.section-title{text-align:center;font-size:23px;color:#444b55}
.incentives .section-title{margin-top:52px}
.cards{position:absolute;top:136px;left:100px;display:flex}
.card{width:200px;height:334px;position:relative;color:var(--white);text-align:center}
.card .label{position:absolute;top:145px;left:0;right:0;font-size:14px;font-weight:700;line-height:1.3}
.card .sub{font-size:11px;font-weight:400;margin-top:12px;line-height:1.5}
.card .more{font-size:11px;font-weight:600;margin-top:14px}

/* plug in */
.plugin{top:1382px;height:508px;background:var(--white)}
.plugin h2{position:absolute;left:100px;top:86px;font-size:27px;color:#555c66}
.feature{position:absolute;width:340px}
.feature h3{font-family:"Open Sans",sans-serif;font-size:14px;font-weight:700;color:var(--blue)}
.feature p{font-size:11px;line-height:1.6;color:var(--muted);margin-top:8px}
.phone{position:absolute;left:828px;top:22px;width:178px;height:460px;border-radius:26px;background:#eef0f3;border:2px solid #d7dbe0;transform:rotate(-6deg)}
.phone .screen{position:absolute;left:12px;top:60px;right:12px;bottom:60px;background:linear-gradient(180deg,#2b1c3c,#5e2a4f 45%,#c24a2a 70%,#211626)}

/* distribution */
.distribution{top:1890px;height:343px;background:linear-gradient(90deg,#0a3fb8,#0a5fe0 60%,#0a3fae)}
.distribution .section-title{color:var(--white);margin-top:48px}
.channel{position:absolute;top:152px;width:220px;text-align:center;color:var(--white)}
.channel h3{font-family:"Open Sans",sans-serif;font-size:14px;font-weight:700;margin-top:14px}
.channel p{font-size:11px;line-height:1.5;margin-top:8px}

/* giveaway */
.giveaway{top:2233px;height:501px}
.giveaway .fill{background:linear-gradient(90deg,#140f0c 0%,#2a1e16 45%,#4a3526 70%,#1b2228 100%)}
.story{position:absolute;color:var(--white)}
.story h2{font-size:27px;line-height:1.3;font-weight:400}
.story p{font-size:11px;line-height:1.6;margin-top:16px}
.giveaway .story{left:100px;top:167px;width:640px}
.giveaway .actions{display:flex;align-items:center;gap:24px;margin-top:28px}
.giveaway .link{font-size:12px;color:#4ea0ff;text-decoration:underline}

/* redemption */
.redemption{top:2734px;height:492px}
.redemption .fill{background:linear-gradient(135deg,#2c2a2a,#6b5e52 40%,#a89786)}
.redemption .panel{position:absolute;left:334px;top:20px;width:866px;height:440px;background:var(--white);transform:rotate(-2deg);transform-origin:left top}
.redemption .story{left:500px;top:165px;width:600px;color:var(--ink);text-align:right}
.redemption .story h2{font-size:23px;color:#3c434c}
.redemption .story p{color:var(--muted)}

/* service */
.service{top:3226px;height:505px}
.service .fill{background:linear-gradient(90deg,#f1eeeb 0%,#e6dcd3 55%,#b88e6c 80%,#8a5c40 100%)}
.service .story{left:100px;top:224px;width:640px;color:var(--ink)}
.service .story h2{font-size:23px;color:#3c434c}
.service .story p{color:var(--muted)}

/* too good */
.too-good{top:3731px;height:522px;background:linear-gradient(180deg,#0b1e4a,#08173a)}
.too-good .story{right:100px;top:185px;width:840px;text-align:right}
.too-good .story h2{font-size:23px}

/* footer */
.site-footer{top:4253px;height:286px;background:var(--footer)}
.footer-col{position:absolute;top:50px;font-size:11px;line-height:21px;color:#9aa4b4;list-style:none}
.footer-col .icon{display:inline-block;width:9px;height:9px;border-radius:50%;background:#5f6b7e;margin-right:8px}
.copyright{position:absolute;left:0;bottom:0;width:1200px;height:44px;line-height:44px;text-align:center;font-size:10px;color:#6f7a8c;background:var(--footer-bottom)}
</style>
</head>
<body>

<section class="section hero">
  <div class="fill" role="img" aria-label="View from an airplane window of a wing over clouds at sunset"></div>
  <header class="topbar">
    <div class="brand"><span class="mark"></span>Brightlane Promo Works</div>
    <nav class="nav">
      <span class="active">Home</span><span>Our Incentives</span><span>Sample</span><span>How it works</span><span>Testimonials</span><span>FAQ</span><span>Contact</span><span>Login</span>
    </nav>
  </header>
  <div class="contact-line"><span>International: 1-800-555-0142</span><span>USA: 555-555-0187</span></div>
  <div class="hero-copy">
    <h1>Increase Leads &amp; Sales From Your Existing Marketing Efforts By Offering High Perceived Value Incentives To Your Customers!</h1>
    <p>Create a variety giveaway promotions for your business with an unlimited supply of top quality vacation getaway certificates, restaurant gift certificates, electronic product giveaways and gas or grocery rewards for just $99/mth.</p>
    <p class="strong">Whether you need 100 or 100,000 you will never pay more than $99.</p>
  </div>
  <div class="hero-actions">
    <a class="btn btn-blue" style="width:207px">Sign Up Risk free for 30 days!</a>
    <a class="btn btn-white" style="width:134px">Learn More</a>
  </div>
</section>

<section class="section stats">
  <div class="stat" style="left:97px">
    <svg width="54" height="44" viewBox="0 0 54 44" fill="none" stroke="#fff" stroke-width="3"><path d="M4 18l12-10 10 6 10-6 14 10-14 14-10-8-10 8z"/></svg>
    <div class="num">12</div><div class="label">Years in Business</div>
  </div>
  <div class="stat" style="left:337px">
    <svg width="44" height="44" viewBox="0 0 44 44" fill="#fff"><circle cx="22" cy="12" r="9"/><path d="M4 44c0-12 8-20 18-20s18 8 18 20z"/></svg>
    <div class="num">13k+</div><div class="label">Clients Enrolled</div>
  </div>
  <div class="stat" style="left:565px">
    <svg width="44" height="44" viewBox="0 0 44 44" fill="none" stroke="#fff" stroke-width="3"><rect x="4" y="6" width="36" height="32" rx="2"/><path d="M12 16h20M12 24h20M12 32h12"/></svg>
    <div class="num">2+</div><div class="label">Million Certificates In Circulation</div>
  </div>
  <div class="stat" style="left:844px">
    <svg width="44" height="44" viewBox="0 0 44 44" fill="none" stroke="#fff" stroke-width="3"><circle cx="22" cy="14" r="10"/><path d="M4 40l10-8h14l10 8"/></svg>
    <div class="num">170k+</div><div class="label">Redemptions To Date</div>
  </div>
</section>

<section class="section incentives">
  <h2 class="section-title">Create Promotional Giveaways Using Any Of These Incentives!</h2>
  <div class="cards">
    <div class="card" role="img" aria-label="Airplane taking off at dusk" style="background:linear-gradient(180deg,#3a4a66,#1c2336)">
      <div class="label">Vacation Getaways<div class="sub">3-7 Nights Including Airfare<br>Up To $2000 Value<br>Your customers just pay taxes</div><div class="more">More Details →</div></div>
    </div>
    <div class="card" role="img" aria-label="Cruise ship at sea" style="background:linear-gradient(180deg,#6f9cc0,#2f5f80)"><div class="label">Cruise Getaways</div></div>
    <div class="card" role="img" aria-label="Couple using a tablet" style="background:linear-gradient(180deg,#c9b8a0,#6d5a48)"><div class="label">Electronic Product<br>Giveaways</div></div>
    <div class="card" role="img" aria-label="Fuel pump at a gas station" style="background:linear-gradient(180deg,#b9746a,#5a3434)"><div class="label">Gas Reward<br>Incentives</div></div>
    <div class="card" role="img" aria-label="Shopper in a grocery aisle" style="background:linear-gradient(180deg,#9e9a7e,#4f4c3b)"><div class="label">Grocery Reward<br>Incentives</div></div>
  </div>
</section>

<section class="section plugin">
  <h2>We plug right into your existing business model in 4 ways</h2>
  <div class="feature" style="left:100px;top:167px"><h3>Advertising</h3><p>Boost response rates from your existing ads by adding one extra hook: "Call for a Free Quote and receive a Three Day Two Night Hotel Stay Certificate to Las Vegas" or 50+ other popular destinations. No Purchase Necessary! Imagine how many more leads you could generate.</p></div>
  <div class="feature" style="left:465px;top:167px"><h3>Residual Business</h3><p>Remind past clients about your products &amp; services with a 2 Night Hotel stay of your previous business clients using a personal touch and an incentive to book.</p></div>
  <div class="feature" style="left:100px;top:308px"><h3>Sales</h3><p>Now that you have generated the lead, try enticing a prospect with an upgrade and offer them Two Nights Plus Airfare if they purchase today. There are so many ways to clinch a deal by offering our incentives as a reward in your closing question.</p></div>
  <div class="feature" style="left:465px;top:308px"><h3>Referrals</h3><p>Contact all of your past customers and offer a Deluxe Vacation Package to anyone who fulfills your request for a new referral. At the end of your sales presentation, offer you have achieved the sale, reduce new clients with a tempting perk if they send you a referral.</p></div>
  <div class="phone" role="img" aria-label="Smartphone showing a city travel certificate at night"><div class="screen"></div></div>
</section>

<section class="section distribution">
  <h2 class="section-title">Easy Distribution</h2>
  <div class="channel" style="left:106px">
    <svg width="50" height="46" viewBox="0 0 50 46" fill="#fff"><rect x="12" y="2" width="26" height="12"/><rect x="2" y="16" width="46" height="18" rx="3"/><rect x="12" y="28" width="26" height="16"/></svg>
    <h3>Print</h3><p>Download PDF certificates to print and physically hand them out or mail them to your customers!</p>
  </div>
  <div class="channel" style="left:361px">
    <svg width="50" height="46" viewBox="0 0 50 46"><rect x="2" y="6" width="46" height="34" fill="#fff"/><path d="M2 6l23 20 23-20" fill="none" stroke="#0a4fc8" stroke-width="3"/></svg>
    <h3>Email</h3><p>Email e-certificates to your customers individually or in bulk with just one click to your closing question.</p>
  </div>
  <div class="channel" style="left:610px">
    <svg width="50" height="46" viewBox="0 0 50 46" fill="#fff"><rect x="2" y="4" width="46" height="30" rx="2"/><rect x="18" y="36" width="14" height="6"/><rect x="10" y="42" width="30" height="3"/></svg>
    <h3>Online Automation</h3><p>Add our web banners on your website. Your customers click on the banner to get free certificates.</p>
  </div>
  <div class="channel" style="left:871px">
    <svg width="50" height="46" viewBox="0 0 50 46" fill="#fff"><path d="M4 4h42v30H18L8 44V34H4z"/></svg>
    <h3>SMS</h3><p>Send area certificates through text messaging with just one click! Coming Soon!</p>
  </div>
</section>

<section class="section giveaway">
  <div class="fill" role="img" aria-label="Black gift box tied with a teal ribbon on a wooden table"></div>
  <div class="story">
    <h2>Give away an unlimited amount of certificates to your customers for just $99 bucks a month.</h2>
    <p>We are A rated with the Regional Business Review Board as well as a licensed seller of travel registered with the State Attorney General (SOT# 0000000). We also participate in the Traveler Protection Reserve Fund (TPRF), which was created to protect consumers from unscrupulous travel companies.</p>
    <div class="actions"><a class="btn btn-white" style="width:161px;color:var(--ink)">Read More</a><span class="link">Sign up now risk free for 30 days</span></div>
  </div>
</section>

<section class="section redemption">
  <div class="fill" role="img" aria-label="Person working on a laptop at a desk"></div>
  <div class="panel"></div>
  <div class="story">
    <h2>Completely Separate Redemption Websites - Online Redemption - Online Reservation Requests</h2>
    <p>First and foremost we're a marketing company and we will protect the integrity of your promotions. By using separate redemption websites keeps your customers from finding out what a great value you are getting. We offer by far what is known as the most end user friendly redemption process in the industry.</p>
    <a class="btn btn-blue" style="width:128px;margin-top:18px">Read More</a>
  </div>
</section>

<section class="section service">
  <div class="fill" role="img" aria-label="Smiling support agent wearing a headset"></div>
  <div class="story">
    <h2>Top Notch Customer Service With Superior Member Support</h2>
    <p>We are easy to contact and we always answer our phone during business hours. We even have a 24 hour live answering service that takes our calls just to guarantee that we never miss a call after hours so if we hop on to back on the other lines.</p>
    <a class="btn btn-blue" style="width:128px;margin-top:22px">Read More</a>
  </div>
</section>

<section class="section too-good">
  <div class="story">
    <h2>TOO GOOD TO BE TRUE! How Do We Do It?</h2>
    <p>Brightlane Promo Works Group, Inc. contracts with the world leading hotel chains and resorts to help fill their otherwise empty rooms when they need it most. We help fill empty rooms which the properties turn into future sales.</p>
    <a class="btn btn-white" style="width:128px;margin-top:24px">Read More</a>
  </div>
</section>

<footer class="section site-footer">
  <ul class="footer-col" style="left:100px"><li>Home</li><li>Our Incentives</li><li>Sample</li><li>How it works</li><li>Testimonials</li><li>FAQ</li><li>Contact</li></ul>
  <ul class="footer-col" style="left:219px"><li>Advertising</li><li>Residual Business</li><li>Sales</li><li>Referrals</li><li>Quick Tour</li><li>Redeem Samples</li><li>Watch Video</li></ul>
  <ul class="footer-col" style="left:371px"><li>Download Brochure</li><li>Reseller Programs</li><li>Terms &amp; Conditions</li><li>Privacy Policy</li><li>Login</li></ul>
  <ul class="footer-col" style="left:529px"><li>Follow Us</li><li><span class="icon"></span>Community</li><li><span class="icon"></span>Updates</li><li><span class="icon"></span>Videos</li></ul>
  <ul class="footer-col" style="left:644px"><li>Contact Us</li><li>International 1-800-555-0142</li><li>USA 555-555-0187</li><li>hello@brightlanepromoworks.biz</li><li>www.brightlanepromoworks.biz</li></ul>
  <ul class="footer-col" style="left:911px;width:190px"><li>About Us</li><li style="line-height:18px">We are A rated with the Regional Business Review Board as well as a licensed seller of travel registered with the State Attorney General. We also participate in the Traveler Protection Reserve Fund.</li></ul>
  <div class="copyright">© 2006-2018 Brightlane Promo Works Group, Inc. – All Rights Reserved. Affiliate Program</div>
</footer>

</body>
</html>
```